Hydrographic business needs a business card that reaches hunters and off-road enthusiasts

We need a business card for a new hydrographics company catering to customers such as hunters, off-road ATV riders and custom vehicle enthusiasts. A western theme is preferred but professional. Our service should be thought of as upper end graphic design on firearms, off road vehicles, motorcycles, etc... See www.caldorfx.com for ideas on patterns, colors, etc...

Target Market(s)

Hunters, off road enthusiasts, custom car enthusiasts, motorcycle riders...

Industry/Entity Type

Graphic Design

```html
<!DOCTYPE html>
<html lang="en">
<head>
<meta charset="utf-8">
<title>Caldor Hydro Graphics – Business Card</title>
<link rel="stylesheet" href="https://fonts.googleapis.com/css2?family=Graduate&family=Roboto+Slab:wght@500;700&display=swap">
<style>
  :root {
    --page: #e7e4dd;
    --ink: #141410;
    --green: #3f9a3c;
    --green-dark: #2f6b2a;
    --cream: #f3ecc8;
    --tan-band: #c79a5e;
    --brown-text: #3d1f0e;
    --back-light: #d7c97e;
    --back-mid: #bfae62;
    --back-warm: #c48a4a;
    --front-light: #c27a3c;
    --front-mid: #b0642c;
    --front-dark: #8d4a22;
  }
  * { box-sizing: border-box; margin: 0; padding: 0; }
  html, body { width: 1200px; height: 1200px; overflow: hidden; }
  body {
    background: var(--page);
    position: relative;
    font-family: "Graduate", serif;
  }
  .card {
    position: absolute;
    left: 150px;
    width: 900px;
    height: 514px;
    overflow: hidden;
    box-shadow: 0 6px 18px rgba(0,0,0,.18);
  }
  .card--back {
    top: 56px;
    background:
      radial-gradient(ellipse at 30% 10%, rgba(196,138,74,.45), transparent 55%),
      radial-gradient(ellipse at 80% 90%, rgba(150,140,70,.35), transparent 60%),
      linear-gradient(160deg, var(--back-light), var(--back-mid));
  }
  .card--front {
    top: 630px;
    background:
      radial-gradient(ellipse at 45% 20%, rgba(214,160,80,.45), transparent 55%),
      linear-gradient(180deg, var(--front-light) 0%, var(--front-mid) 55%, var(--front-dark) 100%);
  }
  .brush-frame { position: absolute; inset: 0; width: 100%; height: 100%; }

  .back-content {
    position: absolute;
    inset: 0;
    display: flex;
    flex-direction: column;
    align-items: center;
    justify-content: center;
    gap: 22px;
    color: var(--green);
    text-align: center;
  }
  .back-content .company { font-size: 30px; letter-spacing: .22em; }
  .back-content .tagline {
    font-family: "Roboto Slab", serif;
    font-weight: 700;
    font-size: 15px;
    letter-spacing: .12em;
  }

  .front-content { position: absolute; left: 0; right: 0; top: 0; bottom: 0; }
  .front-content .company {
    position: absolute;
    left: 150px; top: 140px;
    color: var(--green);
    font-size: 26px;
    letter-spacing: .12em;
  }
  .name-band {
    position: absolute;
    left: 150px; top: 184px;
    width: 620px; height: 68px;
    background: var(--cream);
    display: flex; align-items: center; justify-content: center;
    color: var(--green-dark);
    font-size: 48px;
    letter-spacing: .12em;
  }
  .title-band {
    position: absolute;
    left: 150px; top: 252px;
    width: 620px; height: 24px;
    background: var(--tan-band);
    display: flex; align-items: center; justify-content: center;
    color: var(--cream);
    font-family: "Roboto Slab", serif;
    font-weight: 700;
    font-size: 15px;
    letter-spacing: .35em;
  }
  .contact {
    position: absolute;
    left: 150px; top: 294px;
    width: 620px;
    color: var(--brown-text);
    font-family: "Roboto Slab", serif;
    font-weight: 500;
    font-size: 15px;
    letter-spacing: .14em;
    line-height: 1.7;
  }
</style>
</head>
<body>

<section class="card card--back" aria-label="Card back">
  <svg class="brush-frame" viewBox="0 0 900 514" aria-hidden="true">
    <path fill="var(--ink)" fill-rule="evenodd"
      d="M40 34 L870 22 L878 490 L26 500 Z
         M84 72 L836 64 L842 446 L74 454 Z"/>
  </svg>
  <div class="back-content">
    <p class="company">CALDOR HYDRO GRAPHICS</p>
    <p class="tagline">THE BEST AND MOST RELIABLE HYDROGRAPHICS SERVICE IN TEXAS</p>
  </div>
</section>

<section class="card card--front" aria-label="Card front">
  <svg class="brush-frame" viewBox="0 0 900 514" aria-hidden="true">
    <path fill="var(--ink)" fill-rule="evenodd"
      d="M34 28 L874 36 L866 496 L22 486 Z
         M80 70 L830 76 L824 450 L70 442 Z"/>
  </svg>
  <div class="front-content">
    <p class="company">CALDOR HYDRO GRAPHICS</p>
    <h1 class="name-band">WADE CALDOR</h1>
    <p class="title-band">DIRECTOR</p>
    <p class="contact">
      812 MESA COUNTY ROAD 4420 RED OAK, TX 75154<br>
      214-555-0187 • WWW.CALDORFX.COM • WADE@CALDORFX.COM
    </p>
  </div>
</section>

</body>
</html>
```